Brackenfold Lane Vineyard website

I need to have our website design done. It is an existing site www.brackenfoldlane.com.au which is based on Wordpress which includes information and online purchasing of our wine. Logo and existing branding are to be maintained but website needs to be improved and open to recommendations for function extensions.

Target Market(s)

Wine drinkers and people wanting to visit or hold and event.
Aged from 25-55, men and women

Industry/Entity Type

Vineyard

Number of Pages Required

5+ page

Font styles to use
Sans Serif

Requirements
Must have
• Incorporate existing logos and styling from bottles.
• See existing website www.brackenfoldlane.com.au

```html
<!DOCTYPE html>
<html lang="en">
<head>
<meta charset="utf-8">
<title>Brackenfold Lane Vineyard</title>
<link href="https://fonts.googleapis.com/css2?family=Open+Sans:ital,wght@0,300;0,400;0,600;0,700;1,400;1,700&display=swap" rel="stylesheet">
<style>
  :root {
    --sidebar-bg: #f3f3f2;
    --ink: #2b2b2b;
    --nav-ink: #3a3a3a;
    --rule: #8a8a8a;
    --box-grey: #cfcfcf;
    --footer-bg: #231f20;
    --footer-ink: #9a9a9a;
    --accent-green: #3d9b2f;
    --caption-bg: rgba(28, 28, 28, 0.82);
    --band-bg: rgba(240, 240, 240, 0.82);
    --scene-tint: rgba(60, 60, 60, 0.07);
  }
  * { box-sizing: border-box; margin: 0; padding: 0; }
  html, body { width: 1200px; height: 576px; overflow: hidden; }
  body { font-family: "Open Sans", Arial, sans-serif; color: var(--ink); position: relative; background: #fff; }

  .sidebar { position: absolute; left: 0; top: 0; width: 227px; height: 550px; background: var(--sidebar-bg); }
  .brand { position: absolute; top: 16px; left: 0; width: 227px; text-align: center; color: #1a1a1a; }
  .brand-dot { width: 30px; height: 30px; border-radius: 50%; background: #1a1a1a; margin: 0 auto 15px; }
  .brand-name { font-size: 15.5px; font-weight: 400; letter-spacing: 0.9px; line-height: 1.1; }
  .brand-sub { font-size: 9px; letter-spacing: 1.5px; margin-top: 5px; }

  .divider { position: absolute; left: 26px; width: 174px; height: 1px; background: var(--rule); }
  .divider::after { content: ""; position: absolute; left: 83px; top: -4px; width: 8px; height: 8px; border-radius: 50%; background: #9c9c9c; box-shadow: 0 0 0 3px var(--sidebar-bg); }
  .divider.top { top: 111px; }
  .divider.bottom { top: 355px; }

  .search-btn { position: absolute; left: 26px; top: 123px; width: 18px; height: 17px; background: #8c8c8c; }
  .cart { position: absolute; left: 177px; top: 123px; }
  .cart-badge { position: absolute; left: 15px; top: 6px; width: 13px; height: 13px; border-radius: 50%; background: var(--accent-green); color: #fff; font-size: 8px; line-height: 13px; text-align: center; font-weight: 600; }

  .main-nav { position: absolute; top: 141px; left: 0; width: 227px; list-style: none; text-align: center; }
  .main-nav li { font-size: 11.5px; color: var(--nav-ink); height: 21.4px; line-height: 21.4px; }

  .newsletter { position: absolute; left: 26px; top: 383px; width: 175px; height: 53px; background: var(--box-grey); padding: 5px 9px; }
  .newsletter-title { font-size: 11.2px; color: #222; }
  .newsletter-form { display: flex; margin-top: 3px; gap: 3px; }
  .newsletter-input { width: 127px; height: 17px; background: #e6e6e6; border: 1px solid #b8b8b8; font: italic 10px "Open Sans", Arial, sans-serif; color: #888; padding: 1px 4px; }
  .newsletter-go { width: 26px; height: 17px; background: #1d1d1d; color: #fff; font-size: 10px; text-align: center; line-height: 17px; }

  .contact { position: absolute; left: 24px; top: 457px; list-style: none; font-size: 9.6px; color: #444; }
  .contact li { display: flex; align-items: flex-start; margin-bottom: 7px; }
  .contact svg { width: 10px; height: 10px; margin-right: 13px; margin-top: 2px; flex: none; fill: var(--accent-green); }
  .contact span { line-height: 1.22; }

  .hero { position: absolute; left: 227px; top: 0; width: 973px; height: 550px;
    background: linear-gradient(115deg, #2f3f2a 0%, #5d5a48 28%, #4d6a34 45%, #6f9a45 68%, #5c8a3a 100%); }
  .hero-caption { position: absolute; left: 639px; top: 362px; width: 248px; height: 49px; background: var(--caption-bg); color: #fff; font-style: italic; font-size: 28px; line-height: 49px; text-align: center; }
  .intro-band { position: absolute; left: 0; top: 430px; width: 973px; height: 120px; background: var(--band-bg); }
  .intro-title { position: absolute; left: 39px; top: 13px; font-size: 16px; font-weight: 700; font-style: italic; color: #111; }
  .intro-text { position: absolute; left: 39px; top: 40px; font-size: 10.8px; font-style: italic; color: #2a2a2a; line-height: 18.5px; }
  .scene-area { position: absolute; left: 561px; top: 50px; width: 372px; height: 70px; background: var(--scene-tint); }

  .site-footer { position: absolute; left: 0; top: 550px; width: 1200px; height: 26px; background: var(--footer-bg); color: var(--footer-ink); font-size: 9.6px; line-height: 26px; padding-left: 25px; }
  .social { position: absolute; left: 1030px; top: 9px; display: flex; gap: 27px; }
  .social span { width: 9px; height: 9px; border-radius: 50%; background: #8a8a8a; }
</style>
</head>
<body>
  <aside class="sidebar">
    <div class="brand">
      <div class="brand-dot"></div>
      <div class="brand-name">BRACKENFOLD LANE</div>
      <div class="brand-sub">VINEYARD</div>
    </div>
    <div class="divider top"></div>

    <div class="search-btn">
      <svg width="18" height="17" viewBox="0 0 18 17"><circle cx="8" cy="7.5" r="3.6" fill="none" stroke="#fff" stroke-width="1.6"/><line x1="10.6" y1="10.1" x2="13.5" y2="13" stroke="#fff" stroke-width="1.8"/></svg>
    </div>
    <div class="cart">
      <svg width="16" height="14" viewBox="0 0 16 14"><path d="M1 1.5h2.3l2 7.5h7.5l1.7-5.5H4.3" fill="none" stroke="#8c8c8c" stroke-width="1.3"/><circle cx="6.3" cy="11.8" r="1.2" fill="#8c8c8c"/><circle cx="12" cy="11.8" r="1.2" fill="#8c8c8c"/></svg>
      <div class="cart-badge">0</div>
    </div>

    <ul class="main-nav">
      <li>Home</li><li>Wine</li><li>Contact Us</li><li>Events</li><li>Gallery</li><li>About Us</li><li>Cart</li><li>Members</li><li>Outlets</li>
    </ul>
    <div class="divider bottom"></div>

    <div class="newsletter">
      <div class="newsletter-title">Subscribe to our newsletter</div>
      <div class="newsletter-form">
        <div class="newsletter-input">E-mail address...</div>
        <div class="newsletter-go">GO</div>
      </div>
    </div>

    <ul class="contact">
      <li><svg viewBox="0 0 10 10"><path d="M5 0.5a3.3 3.3 0 0 0-3.3 3.3C1.7 6.3 5 9.7 5 9.7s3.3-3.4 3.3-5.9A3.3 3.3 0 0 0 5 0.5zm0 4.6a1.3 1.3 0 1 1 0-2.6 1.3 1.3 0 0 1 0 2.6z"/></svg><span>12 Brackenfold Lane,<br>Marrenby, NSW 2690,<br>Australia</span></li>
      <li><svg viewBox="0 0 10 10"><path d="M2.2 0.8l1.6 2-0.9 1.2c0.6 1.3 1.6 2.3 2.9 2.9l1.2-0.9 2 1.6-1 1.6C4.9 9.4 0.6 5.1 0.6 1.8z"/></svg><span>+61 400 555</span></li>
      <li><svg viewBox="0 0 10 10"><path d="M0.5 2h9v6.2h-9z M0.5 2.4L5 5.6 9.5 2.4" stroke="#fff" stroke-width="0.7"/></svg><span>wine@brackenfoldlane.com.au</span></li>
    </ul>
  </aside>

  <main class="hero" role="img" aria-label="Aerial photograph of the vineyard in spring: a brick cellar door and water tank beside rows of green vines">
    <div class="hero-caption">Springtime View</div>
    <section class="intro-band">
      <h1 class="intro-title">JOIN US ON THE JOURNEY</h1>
      <p class="intro-text">
        You’ll find our boutique vineyard a little way along the road high on the Lake Marren Escarpment.<br>
        Everything is lovingly handpicked and made locally to produce high quality wine,<br>
        that the Marren District is fast becoming renowned for producing.<br>
        Enjoy with friends, family and the neighbours!
      </p>
      <div class="scene-area" role="img" aria-label="Silhouette illustration of a farm gate on a hill with birds and a dog"></div>
    </section>
  </main>

  <footer class="site-footer">
    Copyright © 2016 Brackenfold Lane Vineyard
    <div class="social"><span></span><span></span><span></span></div>
  </footer>
</body>
</html>
```